Card Design for my dog training business Rustpaw Obedience

Need a business card design for my dog training business with my new logo. Want the card to come off professional yet fun. Want it to be very eye catchy as well. I normally have these at vet clinics, pet stores, and groomers. so need it to look better than my competitors.
Target Market(s)
dog owners
Industry/Entity Type
Dog Training
Contact Information for Business Card
needs logo, my name and info
Font styles to use
Serif
Colors
0255a3
ffffff
ec1f27
000000
333333
fbfbfb
Requirements
Must have
- Rustpaw Obedience
- Hollis Brandt
- 415 903 2267
- info@rustpawobedience.example
- www.rustpawobedience.example

```html
<!DOCTYPE html>
<html lang="en">
<head>
<meta charset="utf-8">
<title>Rustpaw Obedience – Business Card</title>
<link href="https://fonts.googleapis.com/css2?family=Cinzel:wght@500&family=EB+Garamond:ital@1&family=Open+Sans:wght@400;700&display=swap" rel="stylesheet">
<style>
  :root {
    --backdrop: #2b2b2b;
    --card: #ffffff;
    --ink: #000000;
    --ink-soft: #333333;
    --band: #2e2e2e;
    --art-light: #e6e6e6;
    --art-dark: #9a9a9a;
  }
  * { box-sizing: border-box; margin: 0; padding: 0; }
  html, body { width: 1200px; height: 959px; overflow: hidden; }
  body { background: var(--backdrop); position: relative; }

  .card {
    position: absolute;
    width: 560px;
    height: 320px;
    background: var(--card);
    overflow: hidden;
  }
  .card--back { left: 320px; top: 110px; }
  .card--front { left: 320px; top: 530px; }

  /* Back side */
  .back__brand {
    position: absolute;
    left: 0; right: 0; top: 110px;
    text-align: center;
    font-family: "Cinzel", serif;
    font-weight: 500;
    font-size: 36px;
    color: var(--ink);
  }
  .back__tagline {
    position: absolute;
    left: 0; right: 0; top: 190px;
    text-align: center;
    font-family: "EB Garamond", serif;
    font-style: italic;
    font-size: 20px;
    color: var(--ink-soft);
  }

  /* Front side */
  .front__brand {
    position: absolute;
    left: 32px; top: 36px;
    font-family: "Cinzel", serif;
    font-weight: 500;
    font-size: 30px;
    line-height: 1.1;
    color: var(--ink);
  }
  .front__contact {
    position: absolute;
    left: 34px; top: 140px;
    font-family: "Open Sans", sans-serif;
    color: var(--ink-soft);
  }
  .front__name { font-weight: 700; font-size: 19px; margin-bottom: 6px; }
  .front__line { font-size: 13px; line-height: 1.55; }
  .front__line b { font-weight: 700; }

  .front__art {
    position: absolute;
    left: 300px; top: 28px;
    width: 236px; height: 238px;
    background: linear-gradient(160deg, var(--art-light), var(--art-dark));
  }
  .front__band {
    position: absolute;
    left: 250px; right: 0; bottom: 0;
    height: 54px;
    background: var(--band);
    display: flex;
    align-items: center;
    justify-content: flex-end;
    padding-right: 22px;
  }
  .front__url {
    font-family: "Open Sans", sans-serif;
    font-size: 14px;
    color: var(--card);
    letter-spacing: 0.3px;
    white-space: nowrap;
  }
</style>
</head>
<body>
  <section class="card card--back" aria-label="Card back">
    <div class="back__brand">Rustpaw Obedience</div>
    <p class="back__tagline">“Building good manners, one happy dog at a time.”</p>
  </section>

  <section class="card card--front" aria-label="Card front">
    <div class="front__brand">Rustpaw<br>Obedience</div>
    <div class="front__contact">
      <p class="front__name">Hollis Brandt</p>
      <p class="front__line"><b>(P)</b> 415 903 2267</p>
      <p class="front__line">info@rustpawobedience.example</p>
    </div>
    <div class="front__art" role="img" aria-label="Illustration of two dogs over a state outline"></div>
    <div class="front__band">
      <span class="front__url">www.rustpawobedience.example</span>
    </div>
  </section>
</body>
</html>
```